Brightline Servicing-work at height professionals

Specializing In:
High Rise Window Washing
Interior atrium maintenance
Dryer vent cleaning
Building maintenance/inspection
Property maintenance
Pressure washing

Portray:experienced team, QLVOM certified technicians,

Needs to portray the rope access industry and window washing via rope access (not bosun chair!)

Pictures are just examples only of our work
Updates

Designs are looking good! Check the brief again. I updated it

Please change “hi-rise to”High Rise” Thanks, and check rest of the brief for updates on spelling and wording Thanks, designs are looking good!

Aswell need a company logo with the designs Thanks

Target Market(s)

High rise property management companies

Industry/Entity Type

Property Maintenance

Contact Information for Business Card

Torren Mabry
Brightline Servicing
Work at height professionals
C:555-302-7816
E:torren@brightlineservicing.co
E:sales@brightlineservicing.co
Serving southern Alberta

Font styles to use
Sans Serif

Colors

Designer to choose colors to be used in the design.

Requirements
Must have
• High Rise Window Washing
• Dryer Vent Cleaning
• Snow Management
• Interior Atriums Maintenance
• Property Maintenance
• QLVOM Certified
Nice to have
• Work at Height Professionals
• For all your property maintenance needs
• A company logo
• Downtown Calgary Alberta background
Should not have
• Bosun chairs
• Hi-rise

```html
<!DOCTYPE html>
<html lang="en">
<head>
<meta charset="utf-8">
<title>Brightline Servicing – Business Card</title>
<link rel="stylesheet" href="https://fonts.googleapis.com/css2?family=Lato:wght@300;400;700;900&display=swap">
<style>
  :root {
    --stage: #5c5c5c;
    --card: #0d0e10;
    --edge: #1b4f9c;
    --brand-blue: #1a5fb8;
    --text-white: #f2f2f2;
    --text-grey: #b9b9b9;
  }
  * { box-sizing: border-box; margin: 0; padding: 0; }
  html, body {
    width: 1200px; height: 900px; overflow: hidden;
    background: var(--stage);
    font-family: "Lato", sans-serif;
  }
  .stage {
    width: 1200px; height: 900px;
    display: flex; flex-direction: column;
    align-items: center; justify-content: center; gap: 50px;
  }
  .card {
    width: 700px; height: 400px;
    background: var(--card);
    border: 1px solid var(--edge);
    box-shadow: 0 10px 30px rgba(0,0,0,.45);
    position: relative;
    color: var(--text-white);
  }

  /* Brand lockup */
  .brand { text-align: center; }
  .brand-name {
    font-weight: 700; color: var(--brand-blue);
    text-transform: uppercase; letter-spacing: .02em;
  }
  .brand-tagline {
    font-weight: 300; color: var(--text-grey);
    letter-spacing: .28em;
  }

  /* Services side */
  .card-services {
    display: flex; flex-direction: column;
    align-items: center; justify-content: center;
  }
  .card-services .brand-name { font-size: 34px; }
  .card-services .brand-tagline { font-size: 17px; margin-top: 6px; }
  .service-list {
    margin-top: 34px; text-align: center;
    font-size: 20px; line-height: 1.55; color: var(--text-white);
  }
  .service-list .dot { color: var(--brand-blue); padding: 0 6px; }

  /* Contact side */
  .card-contact { display: flex; align-items: center; }
  .card-contact .brand {
    width: 320px; padding-left: 30px;
  }
  .card-contact .brand-name { font-size: 22px; }
  .card-contact .brand-tagline { font-size: 12px; margin-top: 6px; letter-spacing: .24em; }
  .divider {
    width: 1px; height: 150px; background: var(--edge);
    margin: 0 38px 0 10px;
  }
  .person-name {
    font-size: 38px; font-weight: 900; color: var(--brand-blue);
  }
  .person-role {
    font-size: 18px; font-weight: 400; letter-spacing: .22em;
    color: var(--text-white); margin-top: 4px;
  }
  .contact-list { list-style: none; margin-top: 22px; }
  .contact-list li {
    display: flex; align-items: center; gap: 12px;
    font-size: 17px; color: var(--text-white); line-height: 1.6;
  }
  .contact-list svg { width: 15px; height: 15px; flex: none; fill: var(--brand-blue); }
</style>
</head>
<body>
<main class="stage">

  <section class="card card-services">
    <div class="brand">
      <p class="brand-name">Brightline Servicing</p>
      <p class="brand-tagline">Work at Height Professionals</p>
    </div>
    <p class="service-list">
      High Rise Window Washing <span class="dot">•</span> Dryer vent cleaning<br>
      Interior atrium maintenance <span class="dot">•</span> Building maintenance/inspection<br>
      Property maintenance <span class="dot">•</span> Pressure washing
    </p>
  </section>

  <section class="card card-contact">
    <div class="brand">
      <p class="brand-name">Brightline Servicing</p>
      <p class="brand-tagline">Work at Height Professionals</p>
    </div>
    <div class="divider"></div>
    <div class="person">
      <p class="person-name">Torren Mabry</p>
      <p class="person-role">Owner</p>
      <ul class="contact-list">
        <li>
          <svg viewBox="0 0 24 24" aria-hidden="true"><path d="M6.6 10.8a15.1 15.1 0 0 0 6.6 6.6l2.2-2.2a1 1 0 0 1 1-.25 11.4 11.4 0 0 0 3.6.57 1 1 0 0 1 1 1V20a1 1 0 0 1-1 1A17 17 0 0 1 3 4a1 1 0 0 1 1-1h3.5a1 1 0 0 1 1 1c0 1.25.2 2.45.57 3.6a1 1 0 0 1-.25 1z"/></svg>
          555-302-7816
        </li>
        <li>
          <svg viewBox="0 0 24 24" aria-hidden="true"><path d="M2 5h20v14H2z M4 7v.5l8 5 8-5V7l-8 5z" fill-rule="evenodd"/></svg>
          torren@brightlineservicing.co
        </li>
        <li>
          <svg viewBox="0 0 24 24" aria-hidden="true"><path d="M2 5h20v14H2z M4 7v.5l8 5 8-5V7l-8 5z" fill-rule="evenodd"/></svg>
          sales@brightlineservicing.co
        </li>
      </ul>
    </div>
  </section>

</main>
</body>
</html>
```